Business card design for Plumbing and Gas fitting company

We need a business card design for our plumbing and gas fitting company using the company logo and director details. Design should be modern and eye-catching however kept reasonably simple. This design should be targeted at commercial businesses/work so professionalism is key.

Target Market(s)

Commercial/business

Industry/Entity Type

Plumbing

Contact Information for Business Card

Warwick Tane
Director
027 815 0937
warwick@harbourlinepipeworks.example
PO Box 8716
Palmerston North 4441

Font styles to use
Sans Serif

Requirements
Must have
• Logo
• Modern
• Kept simple
Nice to have
• Colour scheme based around logo

```html
<!DOCTYPE html>
<html lang="en">
<head>
<meta charset="utf-8">
<title>Harbourline Pipeworks – Business Cards</title>
<link rel="stylesheet" href="https://fonts.googleapis.com/css2?family=Mulish:wght@400;600;700;800&display=swap">
<style>
  :root {
    --backdrop: #d9dee6;
    --card: #f7f8f8;
    --ink-grey: #6d6e70;
    --brand-blue: #1e73be;
    --brand-orange: #e2793a;
    --rule-orange: #efb58f;
  }
  * { box-sizing: border-box; margin: 0; padding: 0; }
  html, body { width: 1200px; height: 675px; overflow: hidden; }
  body {
    background: var(--backdrop);
    font-family: "Mulish", Arial, sans-serif;
    position: relative;
  }
  .card {
    position: absolute;
    width: 520px;
    height: 297px;
    background: var(--card);
    box-shadow: 0 10px 28px rgba(40, 55, 80, 0.18);
    overflow: hidden;
  }
  .card--front { left: 50px; top: 189px; }
  .card--back { left: 630px; top: 189px; }

  /* Front */
  .front__brand {
    position: absolute;
    left: 0; right: 0; top: 104px;
    display: flex; align-items: center; justify-content: center; gap: 12px;
  }
  .brand-dot {
    width: 20px; height: 20px; border-radius: 50%;
    background: var(--brand-orange);
  }
  .brand-name {
    font-weight: 800;
    color: var(--brand-blue);
    font-size: 30px;
    letter-spacing: 0.3px;
  }
  .front__web {
    position: absolute;
    left: 0; right: 0; top: 176px;
    text-align: center;
    color: var(--ink-grey);
    font-size: 15px;
    letter-spacing: 0.6px;
  }

  /* Back */
  .back__brand {
    position: absolute;
    right: 30px; top: 40px;
    display: flex; align-items: center; gap: 9px;
  }
  .back__brand .brand-name { font-size: 22px; }
  .back__brand .brand-dot { width: 15px; height: 15px; }
  .back__rule {
    position: absolute;
    left: 195px; right: 30px; top: 118px;
    height: 1px; background: var(--rule-orange);
  }
  .back__tab {
    position: absolute;
    left: 0; top: 104px;
    width: 12px; height: 40px;
    background: var(--brand-orange);
    border-radius: 0 5px 5px 0;
  }
  .person { position: absolute; left: 40px; top: 100px; }
  .person__name {
    color: var(--brand-blue);
    font-size: 22px; font-weight: 600;
  }
  .person__role {
    color: var(--ink-grey);
    font-size: 15px; letter-spacing: 0.8px;
    margin-top: 1px; padding-left: 8px;
  }
  .contact {
    position: absolute; left: 48px; top: 170px;
    list-style: none; color: var(--ink-grey); font-size: 15px;
  }
  .contact li { display: flex; align-items: center; gap: 9px; height: 22px; }
  .contact svg { width: 16px; height: 14px; fill: var(--brand-blue); }
  .contact .address { margin-top: 12px; font-size: 16px; letter-spacing: 0.3px; }
  .back__band {
    position: absolute; left: 0; bottom: 0;
    width: 520px; height: 26px;
  }
</style>
</head>
<body>
  <section class="card card--front" aria-label="Card front">
    <div class="front__brand">
      <span class="brand-dot"></span>
      <span class="brand-name">Harbourline Pipeworks</span>
    </div>
    <p class="front__web">www.harbourlinepipeworks.example</p>
  </section>

  <section class="card card--back" aria-label="Card back">
    <div class="back__brand">
      <span class="brand-dot"></span>
      <span class="brand-name">Harbourline Pipeworks</span>
    </div>
    <div class="back__rule"></div>
    <div class="back__tab"></div>
    <div class="person">
      <p class="person__name">Warwick Tane</p>
      <p class="person__role">DIRECTOR</p>
    </div>
    <ul class="contact">
      <li>
        <svg viewBox="0 0 16 14" aria-hidden="true"><path d="M1 4.5C1 2 4 1 8 1s7 1 7 3.5v1.2h-3.2V4.3c-1-.5-2.3-.7-3.8-.7s-2.8.2-3.8.7v1.4H1z"/><path d="M3.5 7 5 5.5h6L12.5 7v6h-9zM8 8a2 2 0 1 0 0 4 2 2 0 0 0 0-4z"/></svg>
        <span>027 815 0937</span>
      </li>
      <li>
        <svg viewBox="0 0 16 14" aria-hidden="true"><path d="M1 2h14v10H1zm1.6 1.2L8 7.6l5.4-4.4zM2.2 4.4v6.4l3.6-3.5zm11.6 0-3.6 2.9 3.6 3.5zM6.7 8l-4 3.8h10.6L9.3 8 8 9z"/></svg>
        <span>warwick@harbourlinepipeworks.example</span>
      </li>
      <li class="address">PO Box 8716, Palmerston North 4441</li>
    </ul>
    <svg class="back__band" viewBox="0 0 520 26" preserveAspectRatio="none" aria-hidden="true">
      <polygon points="0,18 270,18 262,26 0,26" fill="var(--brand-blue)"/>
      <polygon points="280,8 520,8 520,26 262,26" fill="var(--brand-orange)"/>
    </svg>
  </section>
</body>
</html>
```